We are looking for Facebook and Instagram templates. To use both platforms we will use square images. We need a template for our posts, not the header image.
Most posts contain multiple images and we need a designoverlay in which we can embed our images.
Attached a screenshot of our website www.velutra.be, our logo in svg and ai. The monkey is our mascotte (excact this monkey, not another).
We offer teambuildings, the style should be fun. Colors are antracite, limegreen and white. I did attache the current layout for posts but we are not happy with this.
If we could have some small design elements (like stickers) we can always create a new layout but is feels the same.
Our website is quite simple, this should also be in these post designs. Simple forms, rounded corners.
Updates

Allow more time for the designers, good work requires more time

Target Market(s)

Teambuilding

Industry/Entity Type

Teambuilding

Other font styles liked:
• RobotoSlab

Requirements
Must have
• If we could have some small design elements (like stickers) we can always create a new layout but is feels the same.
Should not have
• Complex design, simple images works best for us

```html
<!DOCTYPE html>
<html lang="nl">
<head>
<meta charset="utf-8">
<title>Velutra De Haven – social post templates</title>
<link rel="stylesheet" href="https://fonts.googleapis.com/css2?family=Exo+2:wght@800&family=Roboto:wght@300;400;700&display=swap">
<style>
  :root {
    --anthracite: #555555;
    --anthracite-dark: #4b4b4b;
    --anthracite-light: #666666;
    --night: #1e1e1e;
    --lime: #b3cf0d;
    --lime-soft: #8fa31a;
    --lime-pale: #e6efb4;
    --white: #ffffff;
  }
  html, body {
    margin: 0;
    padding: 0;
    width: 1198px;
    height: 1200px;
    overflow: hidden;
    background: var(--white);
  }
  .sheet {
    position: relative;
    width: 1198px;
    height: 1200px;
  }
  .post {
    position: absolute;
    width: 571px;
    height: 571px;
    display: block;
  }
  .post--split   { left: 23px;  top: 25px; }
  .post--stacked { left: 609px; top: 25px; }
  .post--blob    { left: 23px;  top: 610px; }
  .post--night   { left: 609px; top: 610px; }

  .title     { font-family: "Roboto", sans-serif; font-weight: 700; font-size: 62px; fill: var(--white); }
  .subtitle  { font-family: "Roboto", sans-serif; font-weight: 300; font-size: 34px; fill: var(--white); }
  .brand     { font-family: "Roboto", sans-serif; font-weight: 700; fill: var(--white); letter-spacing: 3px; }
  .display   { font-family: "Exo 2", sans-serif; font-weight: 800; font-size: 76px; }
  .display--pale { fill: var(--lime-pale); }
  .display--lime { fill: var(--lime); }
</style>
</head>
<body>
<main class="sheet">

  <!-- Post layout: split circles -->
  <svg class="post post--split" viewBox="0 0 810 810" xmlns="http://www.w3.org/2000/svg">
    <defs>
      <linearGradient id="barScene1" x1="0" y1="0" x2="1" y2="1">
        <stop offset="0" stop-color="#2e241c"/><stop offset=".55" stop-color="#6b4a2e"/><stop offset="1" stop-color="#3f7a3a"/>
      </linearGradient>
      <linearGradient id="forestScene1" x1="0" y1="0" x2="0" y2="1">
        <stop offset="0" stop-color="#3d6a2a"/><stop offset=".5" stop-color="#8a5a48"/><stop offset="1" stop-color="#cfc8b6"/>
      </linearGradient>
    </defs>
    <rect width="810" height="810" fill="var(--anthracite)"/>
    <path d="M810 0 L810 783 L410 783 C430 560 520 180 810 0 Z" fill="var(--anthracite-dark)"/>
    <circle cx="754" cy="365" r="300" fill="url(#barScene1)" stroke="var(--white)" stroke-width="3" role="img" aria-label="Foto: gasten aan de bar"/>
    <circle cx="514" cy="585" r="140" fill="url(#forestScene1)" stroke="var(--lime)" stroke-width="4" role="img" aria-label="Foto: touwtrekken in kilts"/>
    <rect x="682" y="628" width="75" height="75" fill="var(--lime-soft)" role="img" aria-label="Decoratief sticker-accent"/>
    <rect x="36" y="50" width="124" height="124" rx="34" fill="var(--lime)" role="img" aria-label="Mascotte aap"/>
    <text class="title" x="50" y="258">Enzet</text>
    <text class="title" x="50" y="330">Bouwverlof</text>
    <rect x="50" y="383" width="60" height="5" fill="var(--lime)"/>
    <text class="subtitle" x="50" y="467">Full house met</text>
    <text class="subtitle" x="50" y="502">de inzet van</text>
    <text class="subtitle" x="50" y="537">de zomervakantie</text>
    <text class="brand" x="50" y="660" font-size="30">VELUTRA</text>
    <text class="brand" x="50" y="696" font-size="22">DE HAVEN</text>
    <rect y="783" width="810" height="27" fill="var(--lime)"/>
  </svg>

  <!-- Post layout: stacked photos -->
  <svg class="post post--stacked" viewBox="0 0 810 810" xmlns="http://www.w3.org/2000/svg">
    <defs>
      <linearGradient id="barScene2" x1="0" y1="0" x2="1" y2="1">
        <stop offset="0" stop-color="#2e241c"/><stop offset=".6" stop-color="#6b4a2e"/><stop offset="1" stop-color="#3f7a3a"/>
      </linearGradient>
      <linearGradient id="forestScene2" x1="0" y1="0" x2="0" y2="1">
        <stop offset="0" stop-color="#3d6a2a"/><stop offset=".5" stop-color="#8a5a48"/><stop offset="1" stop-color="#cfc8b6"/>
      </linearGradient>
    </defs>
    <rect width="810" height="810" fill="var(--anthracite)"/>
    <rect x="609" width="201" height="810" fill="var(--anthracite-light)"/>
    <text class="brand" x="50" y="130" font-size="30">VELUTRA</text>
    <text class="brand" x="50" y="162" font-size="22">DE HAVEN</text>
    <text class="title" x="51" y="305">Enzet</text>
    <text class="title" x="51" y="365">Bouwverlof</text>
    <rect x="51" y="440" width="60" height="5" fill="var(--lime)"/>
    <text class="subtitle" x="51" y="537" font-size="36">Full house met</text>
    <text class="subtitle" x="51" y="577" font-size="36">de inzet van</text>
    <text class="subtitle" x="51" y="617" font-size="36">de zomervakantie</text>
    <rect x="414" y="82" width="352" height="297" rx="24" fill="url(#barScene2)" stroke="var(--white)" stroke-width="2" role="img" aria-label="Foto: gasten aan de bar"/>
    <rect x="414" y="403" width="352" height="297" rx="24" fill="url(#forestScene2)" stroke="var(--white)" stroke-width="2" role="img" aria-label="Foto: touwtrekken in kilts"/>
    <rect x="326" y="635" width="155" height="150" rx="40" fill="var(--lime)" role="img" aria-label="Mascotte aap"/>
    <rect y="783" width="810" height="27" fill="var(--lime)"/>
  </svg>

  <!-- Post layout: lime blob with photo row -->
  <svg class="post post--blob" viewBox="0 0 810 810" xmlns="http://www.w3.org/2000/svg">
    <defs>
      <linearGradient id="barScene3" x1="0" y1="0" x2="1" y2="1">
        <stop offset="0" stop-color="#2e241c"/><stop offset=".6" stop-color="#6b4a2e"/><stop offset="1" stop-color="#3f7a3a"/>
      </linearGradient>
      <linearGradient id="forestScene3" x1="0" y1="0" x2="0" y2="1">
        <stop offset="0" stop-color="#3d6a2a"/><stop offset=".5" stop-color="#8a5a48"/><stop offset="1" stop-color="#cfc8b6"/>
      </linearGradient>
      <linearGradient id="footFade" x1="0" y1="0" x2="1" y2="0">
        <stop offset="0" stop-color="var(--lime)"/><stop offset=".7" stop-color="#6f7d0a"/><stop offset="1" stop-color="#111"/>
      </linearGradient>
    </defs>
    <rect width="810" height="810" fill="var(--anthracite)"/>
    <path d="M0 0 H300 C305 60 240 70 170 80 C90 90 40 110 0 138 Z" fill="var(--lime)"/>
    <path d="M0 662 C200 655 600 690 810 655 V810 H0 Z" fill="var(--lime)"/>
    <rect y="782" width="810" height="28" fill="url(#footFade)"/>
    <text class="brand" x="545" y="90" font-size="32">VELUTRA</text>
    <text class="brand" x="545" y="124" font-size="24">DE HAVEN</text>
    <text class="display display--pale" x="52" y="219" textLength="266" lengthAdjust="spacingAndGlyphs">ENZET</text>
    <text class="display display--lime" x="52" y="291" textLength="583" lengthAdjust="spacingAndGlyphs">BOUWVERLOF</text>
    <text class="subtitle" x="51" y="347" font-size="32">Full house met de inzet van</text>
    <text class="subtitle" x="51" y="382" font-size="32">de zomervakantie</text>
    <rect x="25" y="427" width="374" height="315" rx="26" fill="url(#barScene3)" stroke="var(--white)" stroke-width="2" role="img" aria-label="Foto: gasten aan de bar"/>
    <rect x="411" y="427" width="374" height="315" rx="26" fill="url(#forestScene3)" stroke="var(--white)" stroke-width="2" role="img" aria-label="Foto: touwtrekken in kilts"/>
    <circle cx="404" cy="589" r="48" fill="var(--night)"/>
    <rect x="372" y="562" width="64" height="54" rx="16" fill="var(--lime)" role="img" aria-label="Mascotte aap"/>
  </svg>

  <!-- Post layout: night -->
  <svg class="post post--night" viewBox="0 0 810 810" xmlns="http://www.w3.org/2000/svg">
    <defs>
      <radialGradient id="nightGlow" cx=".1" cy=".05" r=".9">
        <stop offset="0" stop-color="#3a4422"/><stop offset=".5" stop-color="#262626"/><stop offset="1" stop-color="var(--night)"/>
      </radialGradient>
      <linearGradient id="barScene4" x1="0" y1="0" x2="1" y2="1">
        <stop offset="0" stop-color="#2e241c"/><stop offset=".6" stop-color="#6b4a2e"/><stop offset="1" stop-color="#3f7a3a"/>
      </linearGradient>
      <linearGradient id="forestScene4" x1="0" y1="0" x2="0" y2="1">
        <stop offset="0" stop-color="#3d6a2a"/><stop offset=".5" stop-color="#8a5a48"/><stop offset="1" stop-color="#cfc8b6"/>
      </linearGradient>
    </defs>
    <rect width="810" height="810" fill="url(#nightGlow)"/>
    <text class="display display--pale" x="406" y="129" text-anchor="middle" textLength="266" lengthAdjust="spacingAndGlyphs">ENZET</text>
    <text class="display display--lime" x="406" y="199" text-anchor="middle" textLength="580" lengthAdjust="spacingAndGlyphs">BOUWVERLOF</text>
    <rect x="349" y="232" width="110" height="105" rx="30" fill="var(--lime)" role="img" aria-label="Mascotte aap"/>
    <text class="subtitle" x="406" y="384" font-size="30" text-anchor="middle">Full house met de inzet van</text>
    <text class="subtitle" x="406" y="419" font-size="30" text-anchor="middle">de zomervakantie</text>
    <path d="M0 449 H378 Q398 449 398 469 V810 H0 Z" fill="url(#barScene4)" role="img" aria-label="Foto: gasten aan de bar"/>
    <path d="M432 449 H810 V810 H412 V469 Q412 449 432 449 Z" fill="url(#forestScene4)" role="img" aria-label="Foto: touwtrekken in kilts"/>
    <text class="brand" x="405" y="626" font-size="36" text-anchor="middle">VELUTRA</text>
    <text class="brand" x="405" y="662" font-size="26" text-anchor="middle">DE HAVEN</text>
  </svg>

</main>
</body>
</html>
```